Weekly Newsletter template for our niche within the Telecom Industry

We need a 'skeleton' format where we can insert our weekly information and ads.
We will do all the content in-house.
Content in both info and ads must be able to contain hyperlinks.
Our company website is: www. halverd-quenby.com
We think we would like something similar to the top format but with the single bar on the right side as a place to insert ads
Thank you.

```html
<!DOCTYPE html>
<html lang="en">
<head>
<meta charset="utf-8">
<title>Halverd Quenby – Weekly Newsletter Template</title>
<link rel="stylesheet" href="https://fonts.googleapis.com/css2?family=Poppins:wght@300;400;500;600&display=swap">
<style>
:root{
  --cyan:#1db4d3;
  --cyan-pale:#dff3f8;
  --lime:#a6cf3a;
  --ink:#2b2d2e;
  --text:#3a3c3e;
  --paper:#ffffff;
  --stage:#ececec;
  --soft:#f4f4f4;
  --rule:#29b3cf;
}
*{margin:0;padding:0;box-sizing:border-box}
html,body{width:901px;height:1200px;overflow:hidden;background:var(--stage)}
body{position:relative;font-family:'Poppins',sans-serif;color:var(--text)}
a{color:inherit;text-decoration:none}
.page{position:absolute;width:357px;height:504px;background:var(--paper);box-shadow:0 2px 6px rgba(0,0,0,.18);overflow:hidden}
.page--cover{left:59px;top:73px}
.page--digest{left:481px;top:73px}
.page--feature{left:275px;top:631px}
.abs{position:absolute}
.accent-bar{position:absolute;width:36px;height:3px;background:linear-gradient(90deg,var(--cyan),var(--lime))}
.h-section{font-weight:500;font-size:16.5px;line-height:17px;color:var(--ink);letter-spacing:-.1px}
.h-sub{font-weight:600;font-size:6.6px;line-height:8px;color:var(--ink);text-transform:uppercase}
.body-copy{font-size:6px;line-height:8.4px;letter-spacing:-.05px;color:var(--text)}
.photo{position:absolute}
.photo--ruled{border-bottom:3px solid var(--cyan)}
.read-more{font-size:5px;color:var(--cyan)}
.web{position:absolute;display:flex;align-items:center;gap:3px;font-size:4.4px;color:var(--text)}
.web svg{width:6px;height:6px}
.brand{position:absolute;display:flex;align-items:center;gap:4px;font-weight:500;color:var(--ink);white-space:nowrap}
.brand-dot{border-radius:50%;background:var(--cyan);flex:none}

/* cover */
.volume{left:24px;top:24px;width:64px;height:15px;background:var(--cyan);color:#fff;font-size:11px;font-weight:300;line-height:15px;padding-left:4px}
.masthead{left:24px;top:49px;font-weight:600;font-size:25px;line-height:28px;color:var(--ink)}
.tagline{left:24px;top:136px;font-weight:300;font-size:13px;color:var(--cyan);letter-spacing:.2px}
.cover-brand{left:248px;top:64px;width:90px;justify-content:center;font-size:8.6px}
.cover-brand .brand-dot{width:9px;height:9px}
.cover-brand-rule{left:248px;top:88px;width:90px;height:4px;background:var(--cyan-pale)}
.sidebar{left:24px;top:173px;width:131px;height:193px;background:var(--cyan);padding:14px 12px;color:#fff}
.sidebar h3{font-weight:500;font-size:12px;margin-bottom:8px}
.sidebar p{font-size:6.5px;line-height:9.6px;font-weight:300;letter-spacing:-.1px}
.cover-main{left:167px;top:173px;width:166px}
.cover-main .h-section{margin-top:10px}
.cover-main .h-sub{margin-top:10px}
.cover-main .body-copy{margin-top:2px}
.checklist{position:absolute;left:167px;top:421px;list-style:none}
.checklist li{display:flex;align-items:center;gap:5px;font-size:6.2px;line-height:9.7px}
.checklist svg{width:5px;height:5px;flex:none}

/* digest */
.digest-top{left:0;top:0;width:357px;height:244px;background:var(--ink)}
.card{position:absolute;top:70px;width:98px}
.card .photo{position:relative;height:80px}
.card .h-sub{color:var(--cyan);margin-top:9px}
.card .body-copy{color:#e6e6e6;font-size:5.8px;line-height:8px;margin-top:2px}
.card .read-more{color:#e6e6e6;display:block;margin-top:3px}
.brief{position:absolute;left:24px;width:241px;height:37px;border-bottom:1px solid var(--rule)}
.brief-inner{border-left:2px solid var(--cyan);padding-left:7px;height:29px}
.brief h4{font-weight:500;font-size:10px;line-height:12px;color:var(--ink)}
.brief p{font-size:5.9px;line-height:6.6px;margin-top:1px;max-width:192px}
.footer-bar{position:absolute;left:0;top:484px;width:357px;height:20px}
.footer-web{left:23px;top:491px}
.footer-web,.footer-web svg{color:#fff}
.footer-brand{right:26px;top:489px;font-size:8px}
.footer-brand .brand-dot{width:8px;height:8px}

/* feature */
.feature-lower{left:0;top:263px;width:357px;height:221px;background:var(--soft)}
.feature-side{left:208px;top:25px;width:131px;height:123px;background:var(--cyan);padding:13px 12px;color:#fff}
.feature-side h3{font-weight:500;font-size:12px;margin-bottom:5px}
.feature-side p{font-size:6.2px;line-height:8.4px;font-weight:300}
.feature-side .read-more{color:#fff;display:block;margin-top:7px}
.feature-top{left:23px;top:22px;width:178px}
.feature-top .h-section{margin-top:10px;max-width:160px}
.feature-lower-copy{left:23px;top:280px;width:305px}
.feature-lower-copy .body-copy{line-height:8.2px}
</style>
</head>
<body>

<!-- Page 1: cover -->
<section class="page page--cover">
  <div class="abs volume">Volume 01</div>
  <h1 class="abs masthead">YOUR<br>COMPANY<br>NEWS LETTER</h1>
  <div class="abs tagline">WEEKLY UPDATE</div>
  <div class="brand cover-brand"><span class="brand-dot"></span>HALVERD QUENBY</div>
  <div class="abs cover-brand-rule"></div>

  <aside class="abs sidebar">
    <h3>Hedding</h3>
    <p>explabora corehenda dolum si occatem accum nim rae velitibus et reped qui ommo optati simusa quam de dolessi bla verrore mpore, que nonse exerit autat estiunt andelestis voluptamus dunt excerios aut ommolest Citaerferrunt ad ut laturit emolore henestias doluptam ipid utemquae et fuga. Ut et a et evelit labo. Enisti ra cus eaque perem que preratqui ad ut eum faccabo. Tis est porum essinte necus. Usa volut quam lautaquibus et, sectore vel inihil ipis exercit</p>
  </aside>
  <div class="photo" role="img" aria-label="Hand touching a glowing digital network interface" style="left:24px;top:371px;width:131px;height:109px;background:radial-gradient(circle at 60% 30%,#6fd3f7 0%,#1b6fb0 35%,#0c2a55 75%,#081a38 100%)"></div>

  <article class="abs cover-main">
    <div class="accent-bar" style="left:0;top:0"></div>
    <h2 class="h-section">This is Heading This is Heading</h2>
    <div class="h-sub">This is sub heading</div>
    <p class="body-copy">Iliquiat urepedi volorrovitia voluptae perovita volupti usdant verum dit dolest laciam eria sent ra doluptaspit rerferum repudip icium, simporiorem rem evel invendigene diae nusa sim quate nis ditatibus samus excessus voluptae verum fugit ipsapit ute volo mo tore sitatendit alicius doluptaqui doluptatio. Et maximinis as della et aut et quia doluptae quis molendi tiuntur, nosapiduciam soluptas inis nulparcium numet idiantiatam, con pediae veliquia quidess equissequi te omnimil etur sam quati repro offic tes et aliquos eatem sed ea abor solupta speria cus. Mus, ulparum esequiae. Nam rem exerione si arit atque ommoditate min nonsedit ea qui raecum acimus cullorum escitem eos expe officipsam, volenimet fugit, non Inum nobit ut esseque volupta sitaquam re modio excerrorero inis minvent.Verempo reptatet aut idi doluptat et magnis asi cus altas il etur sam quati repro offic tes et aliquos eatem sed ea abor solupta speria cus. Mus, ulparum esequiae. Nam rem exerione si arit atque ommoditate min nonsedit ea qui raecum acimus cullorum escitem eos expe officipsam, volenimet fugit, non.</p>
  </article>
  <ul class="checklist">
    <li><svg viewBox="0 0 10 10"><circle cx="5" cy="5" r="5" fill="#1db4d3"/><path d="M2.8 5.2l1.6 1.6 3-3.2" stroke="#fff" stroke-width="1.3" fill="none"/></svg>Verempo reptatet: magnis asi cus alitas</li>
    <li><svg viewBox="0 0 10 10"><circle cx="5" cy="5" r="5" fill="#1db4d3"/><path d="M2.8 5.2l1.6 1.6 3-3.2" stroke="#fff" stroke-width="1.3" fill="none"/></svg>Verempo reptatet: magnis asi cus alitas</li>
    <li><svg viewBox="0 0 10 10"><circle cx="5" cy="5" r="5" fill="#1db4d3"/><path d="M2.8 5.2l1.6 1.6 3-3.2" stroke="#fff" stroke-width="1.3" fill="none"/></svg>Verempo reptatet: magnis asi cus alitas</li>
    <li><svg viewBox="0 0 10 10"><circle cx="5" cy="5" r="5" fill="#1db4d3"/><path d="M2.8 5.2l1.6 1.6 3-3.2" stroke="#fff" stroke-width="1.3" fill="none"/></svg>Verempo reptatet: magnis asi cus alitas</li>
    <li><svg viewBox="0 0 10 10"><circle cx="5" cy="5" r="5" fill="#1db4d3"/><path d="M2.8 5.2l1.6 1.6 3-3.2" stroke="#fff" stroke-width="1.3" fill="none"/></svg>Verempo reptatet: magnis asi cus alitas</li>
    <li><svg viewBox="0 0 10 10"><circle cx="5" cy="5" r="5" fill="#1db4d3"/><path d="M2.8 5.2l1.6 1.6 3-3.2" stroke="#fff" stroke-width="1.3" fill="none"/></svg>Verempo reptatet: magnis asi cus alitas</li>
  </ul>

  <a class="web" href="#" style="left:24px;top:490px"><svg viewBox="0 0 10 10" fill="none" stroke="#1db4d3" stroke-width=".9"><circle cx="5" cy="5" r="4.4"/><ellipse cx="5" cy="5" rx="2" ry="4.4"/><path d="M.6 5h8.8"/></svg>www. halverd-quenby.com</a>
</section>

<!-- Page 2: digest -->
<section class="page page--digest">
  <div class="abs digest-top"></div>
  <div class="accent-bar" style="left:23px;top:30px"></div>
  <h2 class="abs h-section" style="left:23px;top:38px;color:#fff">This is Heading This is Heading</h2>

  <article class="card" style="left:23px">
    <div class="photo photo--ruled" role="img" aria-label="Stacked coins with percent sign and stock chart" style="background:linear-gradient(160deg,#cfd8e4 0%,#8a98ab 45%,#b88a4a 80%,#6b4a22 100%)"></div>
    <div class="h-sub">This is sub heading</div>
    <p class="body-copy">Iliquiat urepedi volorrovitia voluptae perovita volupti usdant verum dit dolest laciam eria sent ra doluptaspit rerferum repudip icium, simporiorem rem evel invendigene diae nusa</p>
    <a class="read-more" href="#">Read More</a>
  </article>
  <article class="card" style="left:130px">
    <div class="photo photo--ruled" role="img" aria-label="Glowing upward arrows on dark blue background" style="background:radial-gradient(circle at 50% 40%,#2a78c9 0%,#0d3f86 50%,#06214d 100%)"></div>
    <div class="h-sub">This is sub heading</div>
    <p class="body-copy">Iliquiat urepedi volorrovitia voluptae perovita volupti usdant verum dit dolest laciam eria sent ra doluptaspit rerferum repudip icium, simporiorem rem evel invendigene diae nusa</p>
    <a class="read-more" href="#">Read More</a>
  </article>
  <article class="card" style="left:237px">
    <div class="photo photo--ruled" role="img" aria-label="Digital padlock on a circuit board" style="background:radial-gradient(circle at 55% 55%,#5fd0ff 0%,#1a74c4 35%,#0b2f60 75%,#061a36 100%)"></div>
    <div class="h-sub">This is sub heading</div>
    <p class="body-copy">Iliquiat urepedi volorrovitia voluptae perovita volupti usdant verum dit dolest laciam eria sent ra doluptaspit rerferum repudip icium, simporiorem rem evel invendigene diae nusa</p>
    <a class="read-more" href="#">Read More</a>
  </article>

  <div class="brief" style="top:273px"><div class="brief-inner"><h4>Denim earumquatiat ulpario. Erias</h4><p>Otatur, cuptassitas dus et et quiatem poribea quatecero conet ullautem quo exeri omnis voluptatur?</p></div></div>
  <div class="brief" style="top:320px"><div class="brief-inner"><h4>Denim earumquatiat ulpario. Erias</h4><p>Otatur, cuptassitas dus et et quiatem poribea quatecero conet ullautem quo exeri omnis voluptatur?</p></div></div>
  <div class="brief" style="top:367px"><div class="brief-inner"><h4>Denim earumquatiat ulpario. Erias</h4><p>Otatur, cuptassitas dus et et quiatem poribea quatecero conet ullautem quo exeri omnis voluptatur?</p></div></div>
  <div class="brief" style="top:414px"><div class="brief-inner"><h4>Denim earumquatiat ulpario. Erias</h4><p>Otatur, cuptassitas dus et et quiatem poribea quatecero conet ullautem quo exeri omnis voluptatur?</p></div></div>

  <svg class="footer-bar" viewBox="0 0 357 20" preserveAspectRatio="none">
    <defs><linearGradient id="slantA" x1="0" y1="1" x2="0" y2="0"><stop offset="0" stop-color="#1db4d3"/><stop offset="1" stop-color="#a6cf3a"/></linearGradient></defs>
    <polygon points="0,0 244,0 238,20 0,20" fill="#2b2d2e"/>
    <polygon points="244,0 247,0 241,20 238,20" fill="url(#slantA)"/>
  </svg>
  <a class="web footer-web" href="#"><svg viewBox="0 0 10 10" fill="none" stroke="#ffffff" stroke-width=".9"><circle cx="5" cy="5" r="4.4"/><ellipse cx="5" cy="5" rx="2" ry="4.4"/><path d="M.6 5h8.8"/></svg>www. halverd-quenby.com</a>
  <div class="brand footer-brand"><span class="brand-dot"></span>HALVERD QUENBY</div>
</section>

<!-- Page 3: feature -->
<section class="page page--feature">
  <div class="abs feature-lower"></div>

  <article class="abs feature-top">
    <div class="accent-bar" style="left:0;top:0"></div>
    <h2 class="h-section">This is Heading This is Heading</h2>
    <div class="h-sub" style="margin-top:6px">This is sub heading</div>
    <p class="body-copy" style="margin-top:1px">Iliquiat urepedi volorrovitia voluptae perovita volupti usdant verum dit dolest laciam eria sent ra doluptaspit rerferum repudip icium, simporiorem rem evel invendigene diae nusa sim quate nis ditatibus samus excessus voluptae verum fugit ipsapit ute volo mo tore sitatendit alicius doluptaqui doluptatio. Et maximinis as della et aut et quia doluptae quis molendi tiuntur, nosapiduciam soluptas inis nulparcium numet idiantiatam, con pediae veliquia quidess equissequi te omnimil etur sam quati repro offic tes et aliquos eatem sed ea abor solupta speria cus. Mus, ulparum esequiae. Nam rem exerione si arit atque ommoditate min nonsedit ea qui raecum acimus cullorum escitem eos expe officipsam, volenimet fugit, non Inum nobit ut esseque volupta sitaquam re modio excerrorero inis minvent.Verempo reptatet aut idi doluptat et magnis asi cus alitas il etur sam quati repro offic tes et aliquos eatem sed ea abor solupta speria cus. Mus, ulparum esequiae. Nam rem exerione si arit atque ommoditate min nonsedit ea qui raecum acimus cullorum escitem eos expe officipsam, volenimet fugit, non</p>
  </article>

  <aside class="abs feature-side">
    <h3>Hedding</h3>
    <p>explabora corehenda dolum si occatem accum nim rae velitibus et reped qui ommo optati simusa quam de dolessi bla verrore mpore, que nonse exerit autat estiunt andelestis voluptamus dunt excerios aut ommolest Citaerferrunt ad ut laturit</p>
    <a class="read-more" href="#">Read More...</a>
  </aside>
  <div class="photo" role="img" aria-label="Telecom tower with wireless signal waves" style="left:208px;top:148px;width:131px;height:100px;background:radial-gradient(circle at 30% 50%,#e6efff 0%,#a9c6f0 40%,#6f97d9 80%,#5a84c8 100%)"></div>

  <article class="abs feature-lower-copy">
    <div class="accent-bar" style="left:0;top:0"></div>
    <h2 class="h-section" style="margin-top:9px">This is Heading This is Heading</h2>
    <div class="h-sub" style="margin-top:5px">This is sub heading</div>
    <p class="body-copy" style="margin-top:1px">Iliquiat urepedi volorrovitia voluptae perovita volupti usdant verum dit dolest laciam eria sent ra doluptaspit rerferum repudip icium, simporiorem rem evel invendigene diae nusa sim quate nis ditatibus samus excessus voluptae verum fugit ipsapit ute volo mo tore sitatendit alicius doluptaqui doluptatio. Et maximinis as della et aut et quia doluptae quis molendi tiuntur, nosapiduciam soluptas inis nulparcium numet idiantiatam, con pediae veliquia quidess equissequi te omnimil etur.</p>
  </article>

  <div class="photo photo--ruled" role="img" aria-label="Night city skyline with 5G network graphics" style="left:23px;top:369px;width:153px;height:93px;background:linear-gradient(180deg,#0d2538 0%,#1c4a66 45%,#3d7a96 70%,#0e2231 100%)"></div>
  <div class="photo photo--ruled" role="img" aria-label="Colleagues celebrating with a high five in an office" style="left:182px;top:369px;width:153px;height:93px;background:linear-gradient(135deg,#6f6a63 0%,#a49a8e 40%,#d8d2c8 65%,#5a5652 100%)"></div>
  <a class="abs read-more" href="#" style="left:23px;top:467px">Read More...</a>
  <a class="abs read-more" href="#" style="left:182px;top:467px">Read More...</a>

  <svg class="footer-bar" viewBox="0 0 357 20" preserveAspectRatio="none">
    <defs><linearGradient id="slantB" x1="0" y1="1" x2="0" y2="0"><stop offset="0" stop-color="#1db4d3"/><stop offset="1" stop-color="#a6cf3a"/></linearGradient></defs>
    <polygon points="0,0 244,0 238,20 0,20" fill="#2b2d2e"/>
    <polygon points="244,0 247,0 241,20 238,20" fill="url(#slantB)"/>
  </svg>
  <a class="web footer-web" href="#"><svg viewBox="0 0 10 10" fill="none" stroke="#ffffff" stroke-width=".9"><circle cx="5" cy="5" r="4.4"/><ellipse cx="5" cy="5" rx="2" ry="4.4"/><path d="M.6 5h8.8"/></svg>www. halverd-quenby.com</a>
  <div class="brand footer-brand"><span class="brand-dot"></span>HALVERD QUENBY</div>
</section>

</body>
</html>
```